An innovative software company needs a business card!

We need a business card design for our new innovative software company. Please use the details for the business card provided in business card details section. We will use the business card paper like: https://www.prindlecard.example/us/products/nfc/business-cards-plus.html Our company name: celvane We have already a logo and colors to use in business cards too ,

Target Market(s)

App & Sofware Development

Industry/Entity Type

Software

Contact Information for Business Card

Lukas Brenner, BSc.
Owner and Creative Superhero

Adress:
Pelzerweg 14/3/1708
A - 1100, Wien

Tel: +43 (0) 664 219 53 08
Email: lukas.brenner@celvane.example
Web: www.celvane.example

Requirements
Must have
• - Use our logo
Nice to have
• It would be nice to have a nice picture on the backside. (About apps, software, technicals or funy stuff) - Use our colors as in business card (optional)

```html
<!DOCTYPE html>
<html lang="en">
<head>
<meta charset="utf-8">
<title>celvane business card</title>
<link rel="stylesheet" href="https://fonts.googleapis.com/css2?family=Open+Sans:wght@400;600;700&display=swap">
<style>
  :root {
    --stage: #2a2c30;
    --brand-blue: #1ca5d0;
    --brand-blue-dark: #1896c0;
    --mark-grey: #b9bcbf;
    --card-white: #ffffff;
    --ink: #1d1d1f;
  }
  * { margin: 0; padding: 0; box-sizing: border-box; }
  html, body {
    width: 1200px; height: 864px; overflow: hidden;
    background: var(--stage);
    font-family: "Open Sans", Arial, sans-serif;
  }
  .canvas { position: relative; width: 1200px; height: 864px; }
  .card {
    position: absolute; left: 320px; width: 560px; height: 340px;
    border-radius: 4px; overflow: hidden;
  }
  .card--front { top: 72px; background: var(--brand-blue); }
  .card--back { top: 452px; background: var(--card-white); }

  .front-wordmark {
    position: absolute; inset: 0;
    display: flex; align-items: center; justify-content: center;
    color: var(--card-white); font-weight: 700; font-size: 72px;
    letter-spacing: 1px;
  }

  .brand {
    position: absolute; right: 36px; top: 62px;
    display: flex; align-items: center; gap: 16px;
    white-space: nowrap;
  }
  .brand__dot {
    width: 56px; height: 56px; border-radius: 50%;
    background: var(--mark-grey); flex: none;
  }
  .brand__name {
    color: var(--brand-blue); font-weight: 700; font-size: 58px;
    line-height: 1; letter-spacing: 1px;
  }

  .person { position: absolute; left: 36px; top: 150px; }
  .person__name {
    color: var(--brand-blue); font-weight: 700; font-size: 20px;
  }
  .person__degree { font-size: 13px; font-weight: 600; }
  .person__title { color: var(--ink); font-size: 13.5px; margin-top: 2px; }

  .divider {
    position: absolute; left: 240px; right: 0; top: 190px;
    height: 2px; background: var(--brand-blue);
  }

  .contact {
    position: absolute; right: 34px; top: 222px;
    list-style: none; text-align: right;
    color: var(--ink); font-size: 14.5px; line-height: 24px;
  }
  .contact__item { display: flex; justify-content: flex-end; align-items: center; gap: 10px; white-space: nowrap; }
  .contact__icon { width: 13px; height: 13px; fill: var(--brand-blue); flex: none; }
  .contact__spacer { width: 13px; flex: none; }
</style>
</head>
<body>
<main class="canvas">
  <section class="card card--front" aria-label="Card front">
    <div class="front-wordmark">celvane</div>
  </section>

  <section class="card card--back" aria-label="Card back">
    <div class="brand">
      <span class="brand__dot"></span>
      <span class="brand__name">celvane</span>
    </div>

    <div class="person">
      <p class="person__name">Lukas Brenner, <span class="person__degree">BSc.</span></p>
      <p class="person__title">Owner and Creative Superhero</p>
    </div>

    <div class="divider"></div>

    <ul class="contact">
      <li class="contact__item">+43 (0) 664 219 53 08
        <svg class="contact__icon" viewBox="0 0 16 16" aria-hidden="true"><path d="M3.2 1.5l2.3-.4 1.4 3.4-1.6 1.2a9 9 0 0 0 5 5l1.2-1.6 3.4 1.4-.4 2.3c-.2.8-1 1.3-1.8 1.2C6.6 13.4 2.6 9.4 2 3.3c-.1-.8.4-1.6 1.2-1.8z"/></svg>
      </li>
      <li class="contact__item">lukas.brenner@celvane.example
        <svg class="contact__icon" viewBox="0 0 16 16" aria-hidden="true"><path d="M1 3h14v10H1z M1.8 3.6L8 8.6l6.2-5" fill="var(--brand-blue)" stroke="#fff" stroke-width="1.2"/></svg>
      </li>
      <li class="contact__item">www.celvane.example
        <svg class="contact__icon" viewBox="0 0 16 16" aria-hidden="true"><circle cx="8" cy="8" r="7"/><path d="M1 8h14M8 1c-3 3.5-3 10.5 0 14M8 1c3 3.5 3 10.5 0 14" fill="none" stroke="#fff" stroke-width="1"/></svg>
      </li>
      <li class="contact__item">Pelzerweg 14/3/1708 A - 1100, Wien<span class="contact__spacer"></span></li>
    </ul>
  </section>
</main>
</body>
</html>
```